KRV Business Cards

We are a local commercial development company based in Silicon Valley and we would like a new business card. I've attached a copy of our company brochure to give a flavor of what we do, our logo, info company colors/graphics, and our current business card. We don't necessarily need a crazy makeover, but would like something that feels a little bit more "fresh" and modern (we've had the same business card design for 15+ years), but still in keeping with our overall brand -- clean, high-quality, modern but timeless. Would like to add our website to the info on the card (www.velmara.com) and would like the flexibility for some folks to have an efax number listed and some not to have that included (without it looking like there is a hole).

```html
<!DOCTYPE html>
<html lang="en">
<head>
<meta charset="utf-8">
<title>KRV Business Cards</title>
<link rel="stylesheet" href="https://fonts.googleapis.com/css2?family=PT+Serif:wght@400;700&family=Roboto:wght@400&display=swap">
<style>
  :root {
    --backdrop: #2b2b2d;
    --card-front: #f1f1f1;
    --navy: #34506a;
    --navy-back: #365068;
    --frame-line: #5a7896;
    --ink: #4e4e4e;
    --rule: #555a60;
    --white: #ffffff;
  }
  * { margin: 0; padding: 0; box-sizing: border-box; }
  html, body { width: 1200px; height: 960px; overflow: hidden; }
  body { background: var(--backdrop); position: relative; }

  .card { position: absolute; width: 600px; height: 343px; box-shadow: 0 3px 8px rgba(0,0,0,.5); }
  .card-front { left: 314px; top: 113px; background: var(--card-front); }
  .card-back { left: 311px; top: 472px; background: var(--navy-back); }

  .company-name {
    font-family: "PT Serif", Georgia, serif;
    font-weight: 400;
    line-height: 1.15;
  }
  .card-front .company-name {
    position: absolute; left: 346px; top: 36px; width: 220px;
    font-size: 26px; color: var(--navy);
  }

  .person { position: absolute; left: 36px; top: 118px; font-family: "PT Serif", Georgia, serif; }
  .person-name { font-size: 22px; font-weight: 700; color: var(--navy); line-height: 1.2; }
  .person-title { font-size: 15px; font-weight: 700; color: var(--navy); line-height: 1.1; }

  .address { position: absolute; left: 36px; top: 173px; font-family: "PT Serif", Georgia, serif; font-size: 15px; color: var(--ink); line-height: 19px; }

  .contacts { position: absolute; left: 36px; top: 216px; list-style: none; font-family: "PT Serif", Georgia, serif; font-size: 15px; color: var(--ink); }
  .contacts li { display: flex; align-items: center; height: 19.3px; }
  .contacts svg { width: 14px; height: 14px; margin-right: 9px; fill: var(--navy); flex: none; }

  .base-rule { position: absolute; left: 0; right: 0; top: 308px; height: 1px; background: var(--rule); }
  .web-badge {
    position: absolute; left: 346px; top: 293px; width: 218px; height: 28px;
    background: var(--navy); border: 2px solid #4d6985;
    color: var(--white); font-family: "Roboto", Arial, sans-serif; font-size: 14px;
    letter-spacing: 1.2px; display: flex; align-items: center; justify-content: center;
  }

  .logo-frame {
    position: absolute; left: 147px; top: 98px; width: 305px; height: 146px;
    border: 1px solid var(--frame-line);
    display: flex; align-items: center; justify-content: center;
  }
  .card-back .company-name {
    font-size: 30px; color: var(--white); text-align: center; width: 250px;
  }
</style>
</head>
<body>
  <section class="card card-front">
    <div class="company-name">KRV Development Company</div>

    <div class="person">
      <div class="person-name">Nora J. Halvorsen</div>
      <div class="person-title">Partner</div>
    </div>

    <div class="address">218 Linden Street<br>Menlo Park, California 94025</div>

    <ul class="contacts">
      <li><svg viewBox="0 0 16 16" aria-hidden="true"><path d="M3.6 1.2 6 3.6 4.7 5.6c.9 2.2 2.6 3.9 4.7 4.8l2-1.3 2.4 2.4-1.5 2.3C7 13.6 2.4 9 2.2 3.1z"/></svg>650.555.0142</li>
      <li><svg viewBox="0 0 16 16" aria-hidden="true"><path d="M4.5 1h7v14h-7zM6 2.5v9.5h4V2.5zM7.3 13h1.4v1H7.3z"/></svg>650.555.0187</li>
      <li><svg viewBox="0 0 16 16" aria-hidden="true"><path d="M4 1h8v4H4zM1 6h14v6h-2v3H3v-3H1zM4.5 10v3.5h7V10z"/></svg>650.555.0263</li>
      <li><svg viewBox="0 0 16 16" aria-hidden="true"><path d="M1 3.5h14v9H1zM2.2 4.4 8 8.6l5.8-4.2z"/></svg>nora@velmara.com</li>
    </ul>

    <div class="base-rule"></div>
    <div class="web-badge">www.velmara.com</div>
  </section>

  <section class="card card-back">
    <div class="logo-frame">
      <div class="company-name">KRV Development Company</div>
    </div>
  </section>
</body>
</html>
```